Innovative IT Company Needs Stationary Design

We require a very professional looking stationary design for "Brightmere Systems", a company that provides specialised IT Consulting Services and Electronic Security and Communication Services.

We require the following Stationary templates as part of this contest:

- Letterhead

- Report template (specifically including a cover page and styles, see the Report Cover Page Example document attached.)

- Business card design (double sided) (We would prefer a business card that makes use of some of the more premium business card printing options, such as foil stamping, embossing/debossing, painted edges, spot UV etc. Doesnt have to use all these things, only what you feel works, but we are looking for a business card that stands out and is memorable and these nice touches have that effect.)

- Envelope

- A4 Display Folder (front and rear design)

We want a sleek, innovative, high end and professional looking design that works well with our new logo (see attached both jpeg and ai versions of our logo). We want the design to feature our logo's colours of blue, grey / silver and black. We also would like to use some crisp lines to compliment our logo. We are also interested in possibly incorporating a faint watermark maybe with blue and grey lines or the logo.

All files should be provided in adobe illustrator, with the exception of the Letterhead and Report templates which should be in MS Word.

The Company details are as follows (I have used one employee as an example):
Company Name: Brightmere Systems Pty Ltd
ABN: 83 604 217 359
Name: Rory Latimer
Title: Technical Director / Solutions Architect
Telephone: +61 8 9302 4161
Mobile: +61 437 265 918
Email: rory.latimer@brightmeresystems.com.au
Website: www.brightmeresystems.com.au

Target Market(s)

Professional Businesses

Industry/Entity Type

Information Technology

Colors
0255a3
cacaca
e8e8e8
000000
ffffff

Requirements
Must have
• - Sleek, Up Market, Feel
• - Use of the exact blue and grey / silver shades in our logo
• - All stationary requested including Letterhead, Report template with cover page and MS word styles, Business Cards double sided, Envelope design, Display folder.
• - ai files to be in 300dpi resolution
• - Report and Letterhead to be in MS Word format
• - Source files upon handover
Nice to have
• - Crisp lines or swirls
• - Watermark
• - Designs that lend themselves to premium printing options such as embossing or foil stamping.
Should not have
• Colours other than blue, grey, silver, black and white

```html
<!DOCTYPE html>
<html lang="en">
<head>
<meta charset="utf-8">
<title>Brightmere Systems – Business Card</title>
<link href="https://fonts.googleapis.com/css2?family=Arimo:wght@400;700&display=swap" rel="stylesheet">
<style>
  :root {
    --brand-blue: #0255a3;
    --deep-blue: #14206b;
    --mid-blue: #1f4fb0;
    --silver: #cacaca;
    --light-grey: #e8e8e8;
    --text-dark: #000000;
    --text-grey: #8a8a8a;
    --white: #ffffff;
  }
  * { margin: 0; padding: 0; box-sizing: border-box; }
  html, body {
    width: 900px;
    height: 1200px;
    overflow: hidden;
    background: var(--white);
    font-family: "Arimo", Arial, sans-serif;
  }
  .canvas {
    position: relative;
    width: 900px;
    height: 1200px;
  }
  .card {
    position: absolute;
    left: 15px;
    width: 870px;
    height: 486px;
    border-radius: 30px;
    overflow: hidden;
  }
  /* Front */
  .card-front {
    top: 90px;
    background: radial-gradient(ellipse at 50% 50%, var(--mid-blue) 0%, #1a3a95 45%, var(--deep-blue) 100%);
    display: flex;
    align-items: center;
    justify-content: center;
  }
  .front-name {
    display: flex;
    align-items: center;
    gap: 22px;
    color: var(--silver);
    font-weight: 700;
    font-size: 46px;
    letter-spacing: 1px;
  }
  .front-name .mark {
    width: 34px;
    height: 34px;
    background: var(--silver);
  }
  /* Back */
  .card-back {
    top: 624px;
    background: var(--white);
    border: 2px solid var(--silver);
  }
  .back-brand {
    position: absolute;
    left: 58px;
    top: 48px;
    display: flex;
    align-items: center;
    gap: 16px;
    color: var(--brand-blue);
    font-weight: 700;
    font-size: 40px;
  }
  .back-brand .mark {
    width: 30px;
    height: 30px;
    background: var(--brand-blue);
  }
  .person {
    position: absolute;
    left: 58px;
    top: 236px;
  }
  .person-name {
    color: var(--brand-blue);
    font-weight: 700;
    font-size: 27px;
  }
  .person-title {
    margin-top: 6px;
    color: var(--text-grey);
    font-size: 20px;
  }
  .contacts {
    position: absolute;
    left: 318px;
    top: 228px;
    list-style: none;
  }
  .contacts li {
    display: flex;
    align-items: center;
    height: 39px;
    font-size: 22px;
    color: var(--text-dark);
  }
  .contacts .icon {
    width: 24px;
    height: 24px;
    margin-right: 48px;
    flex: none;
  }
  .contacts .abn {
    padding-left: 0;
  }
  .bottom-band {
    position: absolute;
    left: 0;
    bottom: 0;
    width: 100%;
    height: 40px;
  }
</style>
</head>
<body>
<main class="canvas">

  <section class="card card-front" aria-label="Business card front">
    <div class="front-name">
      <span class="mark"></span>
      <span>Brightmere Systems</span>
    </div>
  </section>

  <section class="card card-back" aria-label="Business card back">
    <div class="back-brand">
      <span class="mark"></span>
      <span>Brightmere Systems</span>
    </div>

    <div class="person">
      <div class="person-name">Rory Latimer</div>
      <div class="person-title">Director</div>
    </div>

    <ul class="contacts">
      <li>
        <svg class="icon" viewBox="0 0 24 24" aria-hidden="true">
          <path d="M3 8 C3 5 7 4 12 4 C17 4 21 5 21 8 L21 10 L17 10 L17 8 L7 8 L7 10 L3 10 Z" fill="#555"/>
          <rect x="6" y="11" width="12" height="9" rx="2" fill="#555"/>
        </svg>
        +61 437 265 918
      </li>
      <li>
        <svg class="icon" viewBox="0 0 24 24" aria-hidden="true">
          <rect x="7" y="2" width="10" height="20" rx="2" fill="none" stroke="#555" stroke-width="2"/>
          <circle cx="12" cy="18" r="1.3" fill="#555"/>
        </svg>
        +61 8 9302 4161
      </li>
      <li>
        <svg class="icon" viewBox="0 0 24 24" aria-hidden="true">
          <rect x="3" y="6" width="18" height="12" fill="#555"/>
          <path d="M3 6 L12 13 L21 6" fill="none" stroke="#fff" stroke-width="1.5"/>
        </svg>
        rory.latimer@brightmeresystems.com.au
      </li>
      <li>
        <svg class="icon" viewBox="0 0 24 24" aria-hidden="true">
          <circle cx="12" cy="12" r="9" fill="none" stroke="#555" stroke-width="2"/>
          <ellipse cx="12" cy="12" rx="4" ry="9" fill="none" stroke="#555" stroke-width="1.5"/>
          <line x1="3" y1="12" x2="21" y2="12" stroke="#555" stroke-width="1.5"/>
        </svg>
        www.brightmeresystems.com.au
      </li>
      <li class="abn">ABN: 83 604 217 359</li>
    </ul>

    <svg class="bottom-band" viewBox="0 0 866 40" preserveAspectRatio="none" aria-hidden="true">
      <defs>
        <linearGradient id="greyBand" x1="0" y1="0" x2="1" y2="0">
          <stop offset="0" stop-color="#9a9a9a"/>
          <stop offset="1" stop-color="#e8e8e8"/>
        </linearGradient>
        <linearGradient id="blueBand" x1="0" y1="0" x2="1" y2="0">
          <stop offset="0" stop-color="#0255a3"/>
          <stop offset="1" stop-color="#14206b"/>
        </linearGradient>
      </defs>
      <rect x="0" y="0" width="866" height="40" fill="url(#greyBand)"/>
      <polygon points="430,40 470,0 866,0 866,40" fill="url(#blueBand)"/>
    </svg>
  </section>

</main>
</body>
</html>
```